Magento e-commerce webdesign

We need a full e-commerce design for a company based in France. The website will sell belts (men / women).
In files, you have our logo. We made a try for a brown visit card, but it's just an idea. The brown color can be used if it looks like leather, warning it MUSN'T look like "brown shit" :)
So you are free with color but never forget we sell belts and it's both for men & women (upmarket). You can make your own colors changes on the logo (only colors).
You'll find 2 wireframes with the home page & the category page. Elements are in french. UPDATED : you have a traduction files, but it would better if you can make it in french.
Photos have to be on a white background.
Carroussel & every pictures of the wireframes area are very importants.
Target Market(s)
Men & women
Fashion peoples
Upmarket
Industry/Entity Type
It Company
Requirements
Must have
- work on the colors
- work on the pictures (carroussel, newsletter, ventes privées, services, category)
- pro & upmarket
Nice to have
- Product detail page
- Texts in french
Should not have
- Shitty brown colors

```html
<!DOCTYPE html>
<html lang="fr">
<head>
<meta charset="utf-8">
<title>boucleo — ceintures homme &amp; femme</title>
<link rel="stylesheet" href="https://fonts.googleapis.com/css2?family=Arimo:wght@400;700&family=Libre+Baskerville&family=Crimson+Text:ital,wght@0,400;1,400;1,600&display=swap">
<style>
:root{
  --cocoa:#4a3324;
  --leather:#5c4332;
  --leather-dark:#3f2c20;
  --saddle:#7b6049;
  --tobacco:#6a4c35;
  --sand:#b3aa9b;
  --cream:#f1efec;
  --line:#dedad5;
  --ink:#333;
  --muted:#6e6e6e;
  --white:#fff;
  --orange:#f4a21c;
  --grey-btn:#8f8f8f;
}
*{box-sizing:border-box;margin:0;padding:0}
html,body{width:1200px;height:1198px;overflow:hidden;background:var(--white)}
body{position:relative;font-family:"Arimo",Arial,sans-serif;color:var(--ink)}
.abs{position:absolute}

/* header */
.brand{left:72px;top:44px;display:flex;align-items:center;gap:12px}
.brand-dot{width:28px;height:28px;border-radius:50%;background:var(--cocoa)}
.brand-name{font-family:"Libre Baskerville",Georgia,serif;font-size:40px;color:var(--cocoa);letter-spacing:1px}
.brand-url{left:106px;top:114px;font-size:12px;color:var(--muted);letter-spacing:2px}
.cart{left:780px;top:62px;height:42px;width:334px;border:1px solid var(--line);border-radius:22px;display:flex;align-items:center;font-family:"Crimson Text",Georgia,serif;font-size:15px;color:var(--muted);box-shadow:0 2px 3px rgba(0,0,0,.08)}
.cart-icon{width:46px;height:46px;border-radius:50%;background:var(--leather-dark);margin-left:-2px;margin-right:18px;display:flex;align-items:center;justify-content:center}
.cart span{margin:0 10px}

/* navigation */
.nav{left:0;top:146px;width:1200px;height:38px;background:var(--leather)}
.nav a{position:absolute;top:0;height:38px;line-height:38px;color:var(--white);text-decoration:none;font-size:14px}
.nav .active{left:80px;width:96px;background:var(--leather-dark);text-align:center}
.nav .account{left:882px;width:114px;background:var(--grey-btn);text-align:center}
.nav .sponsor{left:998px;width:116px;background:#767676;text-align:center}
.crumb{left:80px;top:196px;font-size:12px;color:var(--ink)}

/* hero */
.hero{left:80px;top:218px;width:736px;height:354px;background:linear-gradient(90deg,#3a2a20,#2c1f17 45%,#2a1d15)}
.hero-photo{position:absolute;left:40px;top:0;width:220px;height:354px;background:linear-gradient(180deg,#8a7767,#5e4a3c 60%,#3a2a20)}
.hero-title{position:absolute;right:46px;top:144px;text-align:right;color:var(--white);font-family:"Crimson Text",Georgia,serif;line-height:1.25}
.hero-title .l1{font-size:40px}
.hero-title .l2{font-size:36px}
.dots{position:absolute;left:614px;top:314px;display:flex;gap:6px}
.dots i{width:16px;height:16px;border-radius:50%;border:1px solid #bbb;background:#3a2a20}
.dots i:first-child{background:#aaa}

/* side panels */
.panel{left:828px;width:286px;color:var(--white);padding:6px 16px}
.panel h2{font-family:"Crimson Text",Georgia,serif;font-style:italic;font-weight:400;font-size:27px;line-height:1.1}
.panel p{font-size:12px;line-height:1.5}
.signup{top:218px;height:112px;background:var(--sand)}
.signup-form{margin-top:10px;display:flex;align-items:center;height:22px;width:234px;background:var(--white);border-radius:11px;color:var(--ink);font-size:11px;padding-left:14px;justify-content:space-between}
.signup-form b{background:var(--leather-dark);color:var(--white);font-weight:400;height:22px;line-height:22px;padding:0 16px;border-radius:11px}
.private{top:340px;height:112px;background:var(--saddle)}
.private h2,.private p{margin-left:114px}
.badge{position:absolute;left:10px;top:10px;width:90px;height:90px;border-radius:50%;background:var(--orange);text-align:center;color:var(--white);font-weight:700;padding-top:18px;line-height:1}
.badge .a{font-size:16px}.badge .b{font-size:26px}
.btn-dark{position:absolute;right:10px;bottom:10px;background:var(--leather-dark);font-size:13px;padding:5px 10px;border-radius:3px}
.services{top:462px;height:110px;background:var(--tobacco)}

/* products */
.product{top:590px;width:198px;height:252px;border:1px solid var(--line);padding:0 10px}
.product-img{height:150px;margin:0 -10px;display:flex;align-items:center;justify-content:center}
.product-img div{width:176px;height:40px;border-radius:6px}
.product h3{font-size:11px;line-height:1.35;color:var(--ink);margin-top:22px}
.price{display:inline-block;margin-top:10px;background:var(--leather-dark);color:var(--white);font-size:11px;padding:4px 8px;border-radius:3px}

/* reassurance */
.info{top:872px;height:98px;border:1px solid var(--line);border-radius:8px;text-align:center;font-size:12px;color:var(--muted)}
.info h4{font-family:"Crimson Text",Georgia,serif;font-style:italic;font-weight:600;font-size:15px;color:var(--ink);text-align:left;padding:10px 0 6px 64px;border-bottom:1px solid var(--line);margin:0 14px 12px}
.info svg{position:absolute;left:12px;top:4px}
.cards{display:flex;gap:8px;justify-content:center}
.cards i{width:42px;height:26px;border:1px solid #ccc;border-radius:3px}
.phone-pill{display:inline-block;background:#e3e3e3;border-radius:12px;padding:3px 26px;color:var(--ink);border-left:34px solid var(--grey-btn);margin-bottom:6px}

/* community */
.soft{top:998px;height:104px;background:var(--cream);border:1px solid #e6e3df;border-radius:10px}
.blog{left:80px;width:510px;padding:14px 20px}
.blog h4{font-family:"Crimson Text",Georgia,serif;font-style:italic;font-weight:400;font-size:19px;color:#999}
.blog p{font-size:11px;line-height:1.55;color:var(--ink);margin-top:10px}
.social{display:flex;align-items:center;justify-content:flex-end;padding-right:26px;font-family:"Crimson Text",Georgia,serif;font-style:italic;font-size:20px;color:#a8a8a8;text-align:center;line-height:1.15}
.social i{position:absolute;left:20px;top:22px;width:58px;height:58px;border-radius:8px;background:#d6d3cf}

/* footer */
.footer{left:0;top:1138px;width:1200px;height:60px;background:var(--leather);color:var(--white);font-size:13px}
.footer .left{position:absolute;left:106px;top:24px;word-spacing:6px}
.footer .right{position:absolute;right:92px;top:24px;word-spacing:4px}
.footer .right span{margin-left:24px}
</style>
</head>
<body>

<header>
  <div class="abs brand"><div class="brand-dot"></div><div class="brand-name">boucleo</div></div>
  <div class="abs brand-url">www.boucleo.com</div>
  <div class="abs cart">
    <div class="cart-icon"><svg width="20" height="16" viewBox="0 0 20 16"><path d="M2 5h16l-2 10H4z" fill="none" stroke="#fff" stroke-width="2"/><path d="M6 5l3-4M14 5l-3-4" stroke="#fff" stroke-width="1.5"/></svg></div>
    0,00 $ <span>|</span> Shopping Basket <span>|</span> Checkout
  </div>
</header>

<nav class="abs nav">
  <a class="active" href="#">HOMME</a>
  <a style="left:222px" href="#">FEMME</a>
  <a style="left:332px" href="#">ACCESSOIRES</a>
  <a class="account" href="#">MON COMPTE</a>
  <a class="sponsor" href="#">PARRAINAGE</a>
</nav>
<div class="abs crumb">Home</div>

<section class="abs hero">
  <div class="hero-photo" role="img" aria-label="Femme blonde en chemise claire portant une ceinture en cuir rouge"></div>
  <div class="hero-title"><div class="l1">Les nouvelles collections</div><div class="l2">deja chez boucleo.com!</div></div>
  <div class="dots"><i></i><i></i><i></i><i></i><i></i></div>
</section>

<aside>
  <div class="abs panel signup">
    <h2>Email Sign Up</h2>
    <p>To receive our exclusive offers and<br>latest product news!</p>
    <div class="signup-form">Enter your email <b>Signup</b></div>
  </div>
  <div class="abs panel private">
    <div class="badge"><div class="a">-25%</div><div class="b">-50%</div></div>
    <h2>Vente Prives</h2>
    <p>To receive our exclusive<br>offers and latest</p>
    <div class="btn-dark">view offers</div>
  </div>
  <div class="abs panel services">
    <h2>Services</h2>
    <p>To receive our exclusive</p>
    <p>Lorem pour recevoir nos</p>
  </div>
</aside>

<section>
  <article class="abs product" style="left:80px">
    <div class="product-img"><div role="img" aria-label="Ceinture en cuir noir" style="background:linear-gradient(#2b2b2b,#111)"></div></div>
    <h3>Ceinture Réversible et Ajustable boucle Ligne Verdon Classique</h3><span class="price">$46.95</span>
  </article>
  <article class="abs product" style="left:290px">
    <div class="product-img"><div role="img" aria-label="Ceinture en cuir taupe" style="background:linear-gradient(#9b8f7a,#716652)"></div></div>
    <h3>Ceinture Réversible et Ajustable boucle Ligne Verdon Classique</h3><span class="price">$46.95</span>
  </article>
  <article class="abs product" style="left:498px">
    <div class="product-img"><div role="img" aria-label="Ceinture en cuir blanc" style="background:linear-gradient(#f4f4f4,#d5d5d5);border:1px solid #ccc"></div></div>
    <h3>Ceinture Réversible et Ajustable boucle Ligne Verdon Classique</h3><span class="price">$46.95</span>
  </article>
  <article class="abs product" style="left:708px">
    <div class="product-img"><div role="img" aria-label="Ceinture en cuir noir verni" style="background:linear-gradient(#333,#0d0d0d)"></div></div>
    <h3>Ceinture Réversible et Ajustable boucle Ligne Verdon Classique</h3><span class="price">$46.95</span>
  </article>
  <article class="abs product" style="left:916px">
    <div class="product-img"><div role="img" aria-label="Ceinture en cuir noir mat" style="background:linear-gradient(#303030,#181818)"></div></div>
    <h3>Ceinture Réversible et Ajustable boucle Ligne Verdon Classique</h3><span class="price">$46.95</span>
  </article>
</section>

<section>
  <div class="abs info" style="left:80px;width:238px">
    <svg width="24" height="30" viewBox="0 0 24 30"><path d="M6 13V8a6 6 0 0 1 12 0v5" fill="none" stroke="#222" stroke-width="3"/><rect x="2" y="13" width="20" height="15" rx="2" fill="#222"/></svg>
    <h4>Paiement CB + virement</h4>
    <div class="cards"><i style="background:#e8ecf5"></i><i style="background:#f6e9e2"></i><i style="background:#e6eef8"></i><i style="background:#eee"></i></div>
  </div>
  <div class="abs info" style="left:344px;width:240px">
    <svg width="36" height="28" viewBox="0 0 36 28"><rect x="2" y="8" width="20" height="14" fill="#222"/><path d="M22 12h7l5 6v4H22z" fill="#222"/><circle cx="9" cy="24" r="3" fill="#222"/><circle cx="28" cy="24" r="3" fill="#222"/></svg>
    <h4>Livraison</h4>
    Votre commande expédiée sous 24h
  </div>
  <div class="abs info" style="left:608px;width:240px">
    <svg width="30" height="30" viewBox="0 0 30 30"><path d="M6 3l6 6-3 4q3 6 8 8l4-3 6 6-4 4Q10 27 2 8z" fill="#222"/></svg>
    <h4>Service client</h4>
    <span class="phone-pill">06 123 456 78</span><br>Service client téléphone et email
  </div>
  <div class="abs info" style="left:872px;width:242px">
    <svg width="24" height="30" viewBox="0 0 24 30"><circle cx="12" cy="8" r="6" fill="#222"/><rect x="3" y="16" width="18" height="12" rx="2" fill="#222"/></svg>
    <h4>Garantie</h4>
    Garantie 10 jours "Satisfait<br>ou Remboursé"
  </div>
</section>

<section>
  <div class="abs soft blog">
    <h4>Derniers articles du blog</h4>
    <p>Lorem Ipsum is simply dummy text of the printing and typesetting industry. Lorem Ipsum has been the industry's standard dummy text ever since the 1500s, when an unknown printer took</p>
  </div>
  <div class="abs soft social" style="left:608px;width:240px"><i></i>Fanpage<br>6715 fans</div>
  <div class="abs soft social" style="left:872px;width:242px"><i></i>Fil 683<br>followers</div>
</section>

<footer class="abs footer">
  <div class="left">CGV | CGU | Plan du site</div>
  <div class="right">© Boucleo <span>Contact Us</span> <span>Privacy Policy</span></div>
</footer>

</body>
</html>
```